Professional Business Card - TWO SIDES

I need a new business card design to be used by myself and my employees. I would like a professional card and for the front I thought I would like a dark blue thatch with our logo in a raised gold foil on top of it. On the other side I would like name, position, and contact info. I've uploaded our old design for an example of the info used.

Target Market(s)

Business Clients

Industry/Entity Type

CPA Firm

Contact Information for Business Card

Logo, Name, Title, Address, Phone Numbers, Website address, Email Address

Font styles to use
Serif
Sans Serif

Colors
0054AA
0677BA
7BADD7
CADEEF
E8F1F8
0094D4
00A9DD
6FCCEA
C7EBF8
E9F6FB

Requirements
Must have
• Modern Professional Look
Nice to have
• Logo in Gold Foil or ability to have is raised. I like our logo in a single color
Should not have
• I've uploaded old business card

```html
<!DOCTYPE html>
<html lang="en">
<head>
<meta charset="utf-8">
<title>Harlow &amp; Harlow – Business Card</title>
<link rel="stylesheet" href="https://fonts.googleapis.com/css2?family=Saira+Condensed:wght@600&family=Mulish:wght@400;800&display=swap">
<style>
  :root {
    --backdrop: #2b2b2d;
    --navy: #163663;
    --gold: #c9a043;
    --paper: #ffffff;
    --ink: #1f2430;
  }
  * { margin: 0; padding: 0; box-sizing: border-box; }
  html, body { width: 1200px; height: 900px; overflow: hidden; }
  body {
    background: var(--backdrop);
    position: relative;
    font-family: "Mulish", sans-serif;
  }
  .card {
    position: absolute;
    left: 250px;
    width: 700px;
    height: 400px;
    overflow: hidden;
  }
  .card--front { top: 35px; background: var(--navy); }
  .card--back  { top: 465px; background: var(--paper); }

  .wordmark {
    font-family: "Saira Condensed", sans-serif;
    font-weight: 600;
    line-height: 1;
    text-transform: uppercase;
  }
  .wordmark__name { display: block; letter-spacing: 1px; }
  .wordmark__tagline { display: block; letter-spacing: 5px; }

  .card--front .wordmark {
    position: absolute;
    left: 0; right: 0; top: 138px;
    text-align: center;
    color: var(--gold);
  }
  .card--front .wordmark__name { font-size: 82px; }
  .card--front .wordmark__tagline { font-size: 22px; margin-top: 8px; }

  .card--back .wordmark {
    position: absolute;
    left: 40px; top: 36px;
    color: var(--navy);
  }
  .card--back .wordmark__name { font-size: 50px; }
  .card--back .wordmark__tagline { font-size: 14px; letter-spacing: 3.6px; margin-top: 4px; }

  .person {
    position: absolute;
    left: 40px; top: 150px;
    padding-left: 22px;
    border-left: 10px solid var(--navy);
  }
  .person__name {
    font-weight: 800;
    font-size: 26px;
    letter-spacing: 1px;
    color: var(--navy);
    text-transform: uppercase;
    line-height: 1.05;
  }
  .person__role { font-size: 16px; color: var(--ink); }

  .contact {
    position: absolute;
    left: 50px; top: 232px;
    list-style: none;
    font-size: 16px;
    color: var(--ink);
    line-height: 1.45;
  }
  .contact__address { margin-bottom: 8px; }
  .contact__line { display: flex; align-items: center; gap: 8px; }
  .contact__icon { width: 14px; height: 14px; fill: var(--navy); flex: none; }

  .brand-disc {
    position: absolute;
    right: 70px; top: 105px;
    width: 220px; height: 220px;
    border-radius: 50%;
    background: var(--navy);
  }
</style>
</head>
<body>

  <section class="card card--front" aria-label="Card front">
    <div class="wordmark">
      <span class="wordmark__name">Harlow &amp; Harlow</span>
      <span class="wordmark__tagline">Certified Public Accountants</span>
    </div>
  </section>

  <section class="card card--back" aria-label="Card back">
    <div class="wordmark">
      <span class="wordmark__name">Harlow &amp; Harlow</span>
      <span class="wordmark__tagline">Certified Public Accountants</span>
    </div>

    <div class="person">
      <p class="person__name">Daniel Reyes</p>
      <p class="person__role">Founder</p>
    </div>

    <ul class="contact">
      <li class="contact__address">1420 N. Alder Street<br>Country Name, AB 35412</li>
      <li class="contact__line">
        <svg class="contact__icon" viewBox="0 0 24 24" aria-hidden="true"><path d="M6.6 10.8a15.1 15.1 0 0 0 6.6 6.6l2.2-2.2a1 1 0 0 1 1-.25 11.4 11.4 0 0 0 3.6.57 1 1 0 0 1 1 1V20a1 1 0 0 1-1 1A17 17 0 0 1 3 4a1 1 0 0 1 1-1h3.5a1 1 0 0 1 1 1c0 1.25.2 2.45.57 3.57a1 1 0 0 1-.25 1z"/></svg>
        (555) 014 2290
      </li>
      <li class="contact__line">
        <svg class="contact__icon" viewBox="0 0 24 24" aria-hidden="true"><path d="M2 5h20v14H2z M3.5 6.5 12 13l8.5-6.5" fill="none" stroke="var(--navy)" stroke-width="2"/></svg>
        info@harlowharlow.com
      </li>
      <li class="contact__line">
        <svg class="contact__icon" viewBox="0 0 24 24" aria-hidden="true"><circle cx="12" cy="12" r="10" fill="none" stroke="var(--navy)" stroke-width="2"/><path d="M2 12h20M12 2c3 3 3 17 0 20M12 2c-3 3-3 17 0 20" fill="none" stroke="var(--navy)" stroke-width="1.6"/></svg>
        www.harlowharlow.com
      </li>
    </ul>

    <div class="brand-disc" aria-hidden="true"></div>
  </section>

</body>
</html>
```